Kestrow-Holdings. Limestone; improving the world

New Limestone company and need logo design.
Limestone offsets carbon mitigation industries restore and replenish soil fertilities in the Prairies, the breadbasket of the world. At the same time, Limestone is proving a critical emergent component of carbon capture sequestration technology will therefore play a critical role in the development of the western Canadian energy industries
Our limestone resources are situated in the foothills of the Canadian Rockies well-positioned above the sprawling fields of the vast peace district.
Target Market(s)
Agriculture and oli sites
Logo Text
Kestrow Holdings
Number of Pages Required
3 page

```html
<!DOCTYPE html>
<html lang="en">
<head>
<meta charset="utf-8">
<title>Kestrow Holdings</title>
<link rel="stylesheet" href="https://fonts.googleapis.com/css2?family=Exo+2:wght@500;600;700&family=Roboto:ital,wght@0,400;0,500;0,700;1,400&display=swap">
<style>
:root{
  --navy:#34506e;
  --blue:#2a9fd0;
  --green:#6ebb1f;
  --ink:#222;
  --text:#555;
  --light:#f2f2f2;
  --white:#fff;
}
*{margin:0;padding:0;box-sizing:border-box}
html,body{width:1200px;height:4062px;overflow:hidden}
body{position:relative;font-family:"Roboto",sans-serif;color:var(--text);background:var(--white)}
.abs{position:absolute}
.heading{font-family:"Exo 2",sans-serif;font-weight:700;text-transform:uppercase;letter-spacing:-0.5px}
.blue{color:var(--blue)}
.center{left:0;width:1200px;text-align:center}
.btn{position:absolute;height:52px;width:190px;border-radius:26px;color:#fff;font-size:15px;font-weight:500;display:flex;align-items:center;justify-content:center;text-transform:uppercase}
.btn-green{background:var(--green)}
.btn-navy{background:var(--navy);box-shadow:0 3px 6px rgba(0,0,0,.25)}

/* top bar */
.topbar{top:0;left:0;width:1200px;height:50px;background:var(--navy)}
.topbar .call{left:676px;top:16px;color:#fff;font-size:14px;display:flex;gap:5px;align-items:center}
.topbar .portal{left:885px;top:0;width:202px;height:50px;background:var(--green);color:#fff;font-size:14px;font-weight:500;display:flex;align-items:center;justify-content:center}

/* nav */
.nav{top:50px;left:0;width:1200px;height:81px;background:#fff}
.brand{left:110px;top:30px;font-family:"Exo 2",sans-serif;font-weight:600;font-size:22px;color:var(--green);text-transform:uppercase;display:flex;align-items:center;gap:8px}
.brand .mark{width:10px;height:10px;background:var(--green)}
.menu{left:444px;top:36px;display:flex;gap:33px;font-size:13px;color:#222;text-transform:uppercase}
.menu .active{color:var(--blue)}

/* hero */
.hero{top:131px;left:0;width:1200px;height:685px;background:linear-gradient(180deg,#b9c6cf 0%,#8f9a8a 22%,#7a7a3c 45%,#3d88a8 62%,#6b6a2c 78%,#8a5a22 100%)}
.hero-title{top:370px;font-size:56px;color:#fff;font-weight:600}
.hero-text{top:440px;color:#fff;font-size:15px;line-height:34px}
.dots{top:772px;left:546px;display:flex;gap:11px}
.dots span{width:12px;height:12px;border-radius:50%;background:#fff}
.dots span.off{background:rgba(255,255,255,.45)}

/* who */
.section-title{font-size:44px;color:var(--ink)}
.who-title{top:906px}
.who-text{top:982px;left:120px;width:960px;text-align:center;font-size:15px;line-height:35px}

/* video */
.video{top:1297px;left:0;width:1200px;height:643px;background:linear-gradient(180deg,#4f6f86 0%,#a49d8c 30%,#b9ac93 60%,#8e7a5c 100%)}
.play{left:548px;top:1566px;width:102px;height:102px;border-radius:50%;background:var(--green);box-shadow:0 0 24px rgba(110,187,31,.7)}

/* sustainability */
.sus-title{top:2105px;left:110px;font-size:44px;color:var(--blue)}
.sus-text{top:2175px;left:112px;width:450px;font-size:15px;line-height:35px}
.frame{left:775px;top:2044px;width:324px;height:222px;background:var(--green)}
.sus-img{left:595px;top:2061px;width:487px;height:414px;background:linear-gradient(180deg,#cfd8d0 0%,#6f8f4a 25%,#5a7d2e 60%,#3f5d22 100%);box-shadow:0 2px 6px rgba(0,0,0,.25)}

/* reviews */
.rev-title{top:2566px}
.rev-text{top:2645px;left:125px;width:950px;text-align:center;font-style:italic;font-size:15px;line-height:35px}
.rev-name{top:2812px;color:var(--green);font-size:17px;font-weight:500;text-transform:uppercase}
.rev-role{top:2843px;font-size:13px}
.arrow{top:2690px;width:48px;height:48px;border:1.5px solid var(--blue);display:flex;align-items:center;justify-content:center}

/* news */
.news{top:2961px;left:0;width:1200px;height:679px;background:var(--light)}
.news-title{top:3017px}
.card{top:3103px;width:317px}
.card .img{height:255px;position:relative}
.card .date{position:absolute;left:0;bottom:0;width:153px;height:45px;background:var(--navy);color:#fff;font-size:15px;display:flex;align-items:center;justify-content:center;gap:5px}
.card h3{margin-top:22px;font-family:"Exo 2",sans-serif;font-weight:600;font-size:16px;color:var(--blue);text-transform:uppercase}
.card p{margin-top:10px;font-size:13px;line-height:28px}

/* footer */
.footer{top:3640px;left:0;width:1200px;height:422px;background:var(--navy);color:#fff}
.f-h{font-weight:500;font-size:17px}
.f-h::after{content:"";display:block;width:40px;height:1px;background:#fff;margin-top:6px}
.f-list{font-size:15px;line-height:43px}
.social{width:46px;height:46px;border-radius:50%;border:1.5px solid #fff}
</style>
</head>
<body>

<header>
  <div class="abs topbar">
    <div class="abs call">
      <svg width="13" height="13" viewBox="0 0 24 24"><path fill="#fff" d="M6.6 10.8a15.1 15.1 0 006.6 6.6l2.2-2.2c.3-.3.7-.4 1-.2 1.1.4 2.3.6 3.6.6.6 0 1 .4 1 1V20c0 .6-.4 1-1 1A17 17 0 013 4c0-.6.4-1 1-1h3.5c.6 0 1 .4 1 1 0 1.3.2 2.5.6 3.6.1.3 0 .7-.2 1z"/></svg>
      CALL NOW - 123-456-7890
    </div>
    <div class="abs portal">CUSTOMER PORTAL</div>
  </div>
  <nav class="abs nav">
    <div class="abs brand"><span class="mark"></span>Kestrow Holdings</div>
    <div class="abs menu">
      <span class="active">Home</span><span>About Us</span><span>Markets</span><span>Locations</span><span>Sustainability</span><span>Careers</span><span>Contact</span>
    </div>
  </nav>
</header>

<section class="abs hero" role="img" aria-label="Aerial view of a city skyline beyond autumn forest and a winding lake"></section>
<h1 class="abs heading hero-title center">Kestrow Holdings</h1>
<p class="abs hero-text center">Lorem ipsum dolor sit amet, consectetur adipiscing elit, sed do eiusmod<br>tempor incididunt ut labore et dolore magna aliqua.</p>
<div class="btn btn-green" style="left:505px;top:519px">Get Started</div>
<div class="abs dots"><span></span><span class="off"></span><span></span><span></span><span></span></div>

<h2 class="abs heading section-title who-title center">Who <span class="blue">We</span> Are</h2>
<p class="abs who-text">Lorem ipsum dolor sit amet, consectetur adipiscing elit, sed do eiusmod tempor incididunt ut labore et dolore magna aliqua. Ut enim ad minim veniam, quis nostrud exercitation ullamco laboris nisi ut aliquip ex ea commodo consequat. Duis aute irure dolor in reprehenderit in voluptate velit esse cillum dolore eu fugiat nulla pariatur. Excepteur sint occaecat cupidatat non proident, sunt in culpa qui officia deserunt mollit anim id est laborum</p>
<div class="btn btn-navy" style="left:505px;top:1140px">Read More</div>

<section class="abs video" role="img" aria-label="Piles of crushed limestone aggregate at a quarry"></section>
<div class="abs play">
  <svg width="102" height="102" viewBox="0 0 102 102"><path fill="#fff" d="M40 30 L72 51 L40 72 Z"/></svg>
</div>

<h2 class="abs heading sus-title">Sustainability</h2>
<p class="abs sus-text">Lorem ipsum dolor sit amet, consectetur adipiscing elit, sed do eiusmod tempor incididunt ut labore et dolore magna aliqua. Ut enim ad minim veniam, quis nostrud exercitation ullamco laboris nisi ut aliquip ex ea commodo consequat. Duis aute irure dolor in reprehenderit in voluptate velit esse cillum</p>
<div class="btn btn-navy" style="left:110px;top:2367px">Read More</div>
<div class="abs frame"></div>
<div class="abs sus-img" role="img" aria-label="Aerial view of wind turbines over green farmland"></div>

<h2 class="abs heading section-title rev-title center">Client <span class="blue">Reviews</span></h2>
<p class="abs rev-text">Lorem ipsum dolor sit amet, consectetur adipiscing elit, sed do eiusmod tempor incididunt ut labore et dolore magna aliqua. Ut enim ad minim veniam, quis nostrud exercitation ullamco laboris nisi ut aliquip ex ea commodo consequat. Duis aute irure dolor in reprehenderit in voluptate velit esse cillum dolore eu fugiat nulla pariatur. Excepteur sint occaecat cupidatat no proident, officia deserunt mollit anim id est laborum</p>
<div class="abs rev-name center">Mara Lindqvist</div>
<div class="abs rev-role center">Lorem ipsum</div>
<div class="abs arrow" style="left:49px"><svg width="20" height="10" viewBox="0 0 20 10"><path d="M19 5H2M6 1 2 5l4 4" stroke="#2a9fd0" stroke-width="2" fill="none"/></svg></div>
<div class="abs arrow" style="left:1100px"><svg width="20" height="10" viewBox="0 0 20 10"><path d="M1 5h17M14 1l4 4-4 4" stroke="#2a9fd0" stroke-width="2" fill="none"/></svg></div>

<section class="abs news"></section>
<h2 class="abs heading section-title news-title center"><span class="blue">Latest</span> News</h2>

<article class="abs card" style="left:110px">
  <div class="img" role="img" aria-label="Hand holding grey limestone rocks" style="background:linear-gradient(160deg,#9a9a9a,#c9a08c 55%,#6f6f6f)">
    <div class="date"><svg width="13" height="13" viewBox="0 0 14 14"><rect x="1" y="2" width="12" height="11" fill="none" stroke="#fff" stroke-width="1.5"/><path d="M1 5h12" stroke="#fff" stroke-width="1.5"/></svg>25-03-2021</div>
  </div>
  <h3>Lorem ipsum dolor sit amet</h3>
  <p>Sed ut perspiciatis unde omnis iste natus error sit voluptatem accusantium doloremque laudantium, totam rem aperiam, eaque ipsa</p>
</article>
<article class="abs card" style="left:441px">
  <div class="img" role="img" aria-label="Aerial view of an open-pit limestone quarry" style="background:linear-gradient(180deg,#7f9a5a,#c8c3b8 40%,#9a958a 75%,#4f7f6a)">
    <div class="date"><svg width="13" height="13" viewBox="0 0 14 14"><rect x="1" y="2" width="12" height="11" fill="none" stroke="#fff" stroke-width="1.5"/><path d="M1 5h12" stroke="#fff" stroke-width="1.5"/></svg>25-03-2021</div>
  </div>
  <h3>Lorem ipsum dolor sit amet</h3>
  <p>Sed ut perspiciatis unde omnis iste natus error sit voluptatem accusantium doloremque laudantium, totam rem aperiam, eaque ipsa</p>
</article>
<article class="abs card" style="left:771px">
  <div class="img" role="img" aria-label="Cut blocks of white limestone in a yard" style="background:linear-gradient(180deg,#e6e8ea,#c9ccd0 50%,#a8acb0)">
    <div class="date"><svg width="13" height="13" viewBox="0 0 14 14"><rect x="1" y="2" width="12" height="11" fill="none" stroke="#fff" stroke-width="1.5"/><path d="M1 5h12" stroke="#fff" stroke-width="1.5"/></svg>25-03-2021</div>
  </div>
  <h3>Lorem ipsum dolor sit amet</h3>
  <p>Sed ut perspiciatis unde omnis iste natus error sit voluptatem accusantium doloremque laudantium, totam rem aperiam, eaque ipsa</p>
</article>
<div class="btn btn-green" style="left:505px;top:3542px">View More</div>

<footer class="abs footer">
  <div class="abs" style="left:110px;top:92px;font-size:21px;font-weight:500">About Us</div>
  <p class="abs" style="left:110px;top:132px;width:290px;font-size:11px;line-height:27px">Lorem ipsum dolor sit amet, consectetur adipiscing elit, sed do eiusmod tempor incididunt dolore magna aliqua. Ut enim ad minim veniam,</p>
  <div class="abs" style="left:110px;top:244px;font-size:15px;font-weight:500">FOLLOW US</div>
  <div class="abs social" style="left:112px;top:289px"></div>
  <div class="abs social" style="left:165px;top:289px"></div>
  <div class="abs social" style="left:217px;top:289px"></div>
  <div class="abs" style="left:440px;top:60px;width:1px;height:290px;background:rgba(255,255,255,.6)"></div>

  <div class="abs f-h" style="left:520px;top:80px">Contact Us</div>
  <div class="abs f-list" style="left:527px;top:118px;line-height:27px">
    <div style="margin-bottom:17px">&#9742; 123-456-7890</div>
    <div>&#9679; Lorem ipsum dolor sit amet<br>Lorem ipsum dolor</div>
    <div style="margin-top:18px">&#9993; KestrowHoldings.com</div>
  </div>

  <div class="abs f-h" style="left:775px;top:80px">Links</div>
  <div class="abs f-list" style="left:781px;top:110px">
    <div>&raquo; Home</div><div>&raquo; About us</div><div>&raquo; Locations</div><div>&raquo; contact us</div>
  </div>

  <div class="abs f-h" style="left:923px;top:80px">Useful Links</div>
  <div class="abs f-list" style="left:930px;top:118px;line-height:32px">
    <div>Sustainability</div><div>Testimonials</div><div>Privacy Policy</div>
  </div>

  <div class="abs" style="left:897px;top:367px;font-size:15px">&copy; 2021 All Rights Reserved</div>
</footer>

</body>
</html>
```